Bramwick Client Journey To Success

I need a one-page document that graphically shows the client's journey working with Bramwick from initial assessment to completed project. I want the journey to start at the "basecamp logo" and reach 4 summits (little mountain logos...) .

I'd like the imagery to convey the client starting at basecamp, and moving to each summit. Each summit, should list the subtext under each, as listed on the pdf doc i provided.

The description for the basecamp and 4 summits is attached.

I need the brochure to look like the other brochure that you did for me (attached) .

Target Market(s)

Restaurant Owners

Industry/Entity Type

Construction Management

Font styles to use
Sans Serif

Colors
EB3D1F
EC4F4E
F09395
F8D3D4
FCEDEE

Requirements
Must have
• My logo. Title: Client Journey To Success. Subtitle: The 4 Summits

```html
<!DOCTYPE html>
<html lang="en">
<head>
<meta charset="utf-8">
<title>Bramwick Development – Client Journey To Success</title>
<link rel="stylesheet" href="https://fonts.googleapis.com/css2?family=Montserrat:wght@400;500;700;800;900&display=swap">
<style>
  :root {
    --red: #e32b28;
    --red-deep: #c81f1d;
    --ink: #222222;
    --text: #3a3a3a;
    --paper: #ffffff;
  }
  * { box-sizing: border-box; margin: 0; padding: 0; }
  html, body {
    width: 977px; height: 1200px; overflow: hidden;
    background: var(--paper);
  }
  .page {
    position: absolute; left: 0; top: 0;
    width: 768px; height: 944px;
    transform: scale(1.2721);
    transform-origin: 0 0;
    font-family: "Montserrat", sans-serif;
    color: var(--text);
  }
  .title {
    position: absolute; left: 36px; top: 38px;
    font-weight: 900; font-size: 21.5px; letter-spacing: 0.1px;
    color: var(--ink); text-transform: uppercase;
  }
  .title-rule {
    position: absolute; left: 36px; top: 69px; width: 382px; height: 6px;
  }
  .title-rule .thick { position: absolute; left: 0; top: 0; width: 252px; height: 6px; background: var(--ink); }
  .title-rule .thin { position: absolute; left: 252px; top: 2px; width: 130px; height: 1px; background: var(--red); }
  .subtitle {
    position: absolute; left: 36px; top: 84px;
    font-weight: 400; font-size: 22px; color: var(--red);
  }
  .brand {
    position: absolute; left: 580px; top: 60px; width: 166px;
    display: flex; flex-direction: column; align-items: center; gap: 14px;
  }
  .brand-mark { width: 86px; height: 86px; background: var(--red); }
  .brand-name {
    font-weight: 800; font-size: 12.5px; color: var(--ink);
    text-transform: uppercase; white-space: nowrap;
  }
  .route { position: absolute; left: 0; top: 0; width: 768px; height: 944px; }
  .stop { position: absolute; }
  .stop-icon { display: block; width: 20px; height: 18px; margin-bottom: 2px; }
  .stop-label {
    font-weight: 800; font-size: 11px; color: var(--red);
    text-transform: uppercase; line-height: 12px;
  }
  .stop-name {
    font-weight: 800; font-size: 17px; color: var(--ink); line-height: 21px;
  }
  .stop-list { list-style: none; margin-top: 1px; }
  .stop-list li {
    position: relative; padding-left: 10px;
    font-size: 13px; line-height: 19.8px; color: var(--text);
  }
  .stop-list li::before {
    content: ""; position: absolute; left: 0; top: 8px;
    width: 4px; height: 4px; border-radius: 50%; background: var(--red);
  }
  .basecamp { left: 56px; top: 205px; }
  .summit-1 { left: 525px; top: 354px; }
  .summit-2 { left: 56px; top: 500px; }
  .summit-3 { left: 525px; top: 646px; }
  .summit-4 { left: 56px; top: 794px; }
</style>
</head>
<body>
<div class="page">
  <h1 class="title">Client Journey To Success</h1>
  <div class="title-rule"><span class="thick"></span><span class="thin"></span></div>
  <p class="subtitle">The 4 Summits</p>

  <div class="brand">
    <span class="brand-mark"></span>
    <span class="brand-name">Bramwick Development</span>
  </div>

  <svg class="route" viewBox="0 0 768 944" aria-hidden="true">
    <g stroke="var(--red)" stroke-width="6" fill="none">
      <polyline points="266,250 451,395 266,540 451,690 266,835"/>
    </g>
    <defs>
      <path id="hex" d="M0,-43 L37,-21.5 L37,21.5 L0,43 L-37,21.5 L-37,-21.5 Z"/>
    </defs>
    <g fill="var(--red)">
      <use href="#hex" x="266" y="250"/>
      <use href="#hex" x="451" y="395"/>
      <use href="#hex" x="266" y="540"/>
      <use href="#hex" x="451" y="690"/>
      <use href="#hex" x="266" y="835"/>
    </g>
    <!-- tent -->
    <g transform="translate(266 250)" fill="#fff">
      <path d="M-20,20 L0,-14 L20,20 L8,20 L0,6 L-8,20 Z"/>
      <path d="M-6,-22 L0,-12 L6,-22" stroke="#fff" stroke-width="3" fill="none"/>
    </g>
    <!-- barrier -->
    <g transform="translate(451 395)" fill="none" stroke="#fff" stroke-width="3">
      <rect x="-20" y="-14" width="40" height="10"/>
      <path d="M-12,-14 L-18,-4 M-2,-14 L-8,-4 M8,-14 L2,-4 M18,-14 L12,-4"/>
      <path d="M-14,-4 V18 M14,-4 V18 M-14,4 H14"/>
    </g>
    <!-- network -->
    <g transform="translate(266 540)" fill="#fff" stroke="#fff" stroke-width="2.5">
      <circle r="7"/>
      <path d="M0,-18 V18 M-16,-9 L16,9 M-16,9 L16,-9"/>
      <circle cx="0" cy="-19" r="4.5"/><circle cx="0" cy="19" r="4.5"/>
      <circle cx="-16.5" cy="-9.5" r="4.5"/><circle cx="16.5" cy="9.5" r="4.5"/>
      <circle cx="-16.5" cy="9.5" r="4.5"/><circle cx="16.5" cy="-9.5" r="4.5"/>
    </g>
    <!-- document with arrows -->
    <g transform="translate(451 690)" fill="none" stroke="#fff" stroke-width="2.5">
      <path d="M-8,-18 H-16 V18 H-2 M8,18 H16 V-18 H2"/>
      <path d="M-6,-18 H6 M2,-22 L6,-18 L2,-14 M6,18 H-6 M-2,14 L-6,18 L-2,22"/>
      <path d="M-9,-7 H9 M-9,0 H9 M-9,7 H3"/>
    </g>
    <!-- flag -->
    <g transform="translate(266 835)">
      <ellipse cx="-2" cy="19" rx="11" ry="4" fill="none" stroke="#fff" stroke-width="2.5"/>
      <path d="M-6,19 V-20" stroke="#fff" stroke-width="3"/>
      <rect x="-5" y="-20" width="20" height="16" fill="#fff"/>
      <g fill="var(--red)">
        <rect x="0" y="-20" width="5" height="4"/><rect x="10" y="-20" width="5" height="4"/>
        <rect x="-5" y="-16" width="5" height="4"/><rect x="5" y="-16" width="5" height="4"/>
        <rect x="0" y="-12" width="5" height="4"/><rect x="10" y="-12" width="5" height="4"/>
        <rect x="-5" y="-8" width="5" height="4"/><rect x="5" y="-8" width="5" height="4"/>
      </g>
    </g>
  </svg>

  <section class="stop basecamp">
    <svg class="stop-icon" viewBox="0 0 20 22" aria-hidden="true">
      <path d="M1,22 L10,6 L19,22 L13,22 L10,16 L7,22 Z M5,0 L10,7 L15,0" fill="var(--red)" stroke="var(--red)" stroke-width="2"/>
    </svg>
    <h2 class="stop-name">Basecamp</h2>
    <ul class="stop-list">
      <li>Client Assessment</li>
      <li>Determine Project Goals</li>
      <li>Proposal &amp; Fees</li>
    </ul>
  </section>

  <section class="stop summit-1">
    <svg class="stop-icon" viewBox="0 0 20 14" aria-hidden="true"><path d="M0,14 L8,2 L11,6 L13,4 L20,14 Z" fill="var(--red)"/></svg>
    <p class="stop-label">Summit 1</p>
    <h2 class="stop-name">PreConstruction</h2>
    <ul class="stop-list">
      <li>Develop Project Plan</li>
      <li>Develop Risk Assessment &amp; Plan</li>
      <li>Devlelop Schedule</li>
      <li>Develop Budget</li>
      <li>Develop Team</li>
      <li>GC, Sub, Consultants Contracts</li>
    </ul>
  </section>

  <section class="stop summit-2">
    <svg class="stop-icon" viewBox="0 0 20 14" aria-hidden="true"><path d="M0,14 L8,2 L11,6 L13,4 L20,14 Z" fill="var(--red)"/></svg>
    <p class="stop-label">Summit 2</p>
    <h2 class="stop-name">Execution</h2>
    <ul class="stop-list">
      <li>Acquire Permits</li>
      <li>PreConstruction Meeting</li>
      <li>Project Start</li>
    </ul>
  </section>

  <section class="stop summit-3">
    <svg class="stop-icon" viewBox="0 0 20 14" aria-hidden="true"><path d="M0,14 L8,2 L11,6 L13,4 L20,14 Z" fill="var(--red)"/></svg>
    <p class="stop-label">Summit 3</p>
    <h2 class="stop-name">Project Management</h2>
    <ul class="stop-list">
      <li>Shared Consciousness Meetings</li>
      <li>Pressurized Collaboration</li>
      <li>Schedule Management</li>
      <li>Run O.O.D.A. Loop</li>
    </ul>
  </section>

  <section class="stop summit-4">
    <svg class="stop-icon" viewBox="0 0 20 14" aria-hidden="true"><path d="M0,14 L8,2 L11,6 L13,4 L20,14 Z" fill="var(--red)"/></svg>
    <p class="stop-label">Summit 4</p>
    <h2 class="stop-name">Completion</h2>
    <ul class="stop-list">
      <li>Closeout</li>
    </ul>
  </section>
</div>
</body>
</html>
```